Powerpoint design for european B2B business

We need a Powerpoint design for a newly established IT company with a B2B focus. We want to develop management information systems that help managers communicate goals into their organization and analyze their organizational activities and performance.

We defined the attached color scale, please relate your design to these colors.

The design should be simple and straight, serious and professional and leave enough space for the content ... :-)

Target Market(s)

B2B, companies larger than 200 employees

Industry/Entity Type

Business

Font styles to use
Sans Serif

Requirements
Should not have
• too playful design, clipart style

```html
<!DOCTYPE html>
<html lang="en">
<head>
<meta charset="utf-8">
<title>Kestrelon – Presentation Template</title>
<link rel="stylesheet" href="https://fonts.googleapis.com/css2?family=Open+Sans:wght@400;600;700&display=swap">
<style>
:root{
  --board:#383838;
  --white:#ffffff;
  --ink:#444a52;
  --title:#3f4349;
  --muted:#6b6f75;
  --navy:#1f3b63;
  --blue:#3b68a6;
  --mid:#4f82c8;
  --cyan:#0aaeea;
  --accent:#b23a2a;
  --line:#4a73ad;
}
*{margin:0;padding:0;box-sizing:border-box}
html,body{width:907px;height:1200px;overflow:hidden;background:var(--board)}
body{position:relative;font-family:"Open Sans",Arial,sans-serif;color:var(--ink)}
.slide{position:absolute;width:307px;height:230px;background:var(--white);overflow:hidden}
.slide-title{position:absolute;left:0;right:0;text-align:center;font-size:10.5px;font-weight:400;letter-spacing:.3px;color:var(--title)}
.subtitle{position:absolute;left:0;right:0;text-align:center;font-size:5px;color:var(--muted)}
.body-text{font-size:5px;line-height:1.55;color:var(--muted);text-align:justify}
.photo{position:absolute}

/* cover */
.cover-photo{inset:0;background:linear-gradient(100deg,#ece8e2 0%,#e2ddd5 55%,#cfc8c0 100%)}
.stripe{position:absolute;top:0;bottom:0;background:rgba(255,255,255,.85)}
.brand-name{position:absolute;left:22px;top:90px;width:140px;text-align:center;font-size:17px;font-weight:600;color:var(--title);letter-spacing:1.5px;line-height:1}

/* intro */
.intro-band{position:absolute;left:0;top:0;width:128px;height:230px;background:var(--blue)}
.intro-band h2{position:absolute;left:19px;top:21px;font-size:10px;font-weight:400;color:var(--white);letter-spacing:.3px}
.avatar{position:absolute;left:171px;top:19px;width:28px;height:28px;border-radius:50%;background:linear-gradient(#9c9c9c,#5c5c5c)}
.author-name{position:absolute;left:204px;top:27px;font-size:4.8px;font-weight:700;color:var(--accent)}
.author-role{position:absolute;left:204px;top:33px;font-size:4.8px;color:#444}
.intro-text{position:absolute;left:150px;top:62px;width:140px;font-size:5.2px;line-height:9px}
.intro-text p+p{margin-top:9px}

/* grid slide */
.tile{position:absolute;width:103px;height:85px;display:flex;align-items:center;justify-content:center;text-align:center;font-size:4.8px;line-height:1.3;color:var(--white);padding:0 15px}
.tile.cyan{background:var(--cyan)}
.tile.blue{background:var(--mid)}

/* services 1 */
.feature-box{position:absolute;left:175px;top:54px;width:117px;height:90px;background:var(--mid);color:var(--white);padding:10px 14px}
.feature-box h3{font-size:5.5px;font-weight:700;margin-bottom:7px}
.feature-box p{font-size:5px;line-height:1.35;text-align:justify}
.services-text{position:absolute;left:20px;top:154px;width:270px}
.services-text p+p{margin-top:5px}

/* icon bubbles */
.icon-ring{position:absolute;width:34px;height:34px;border-radius:50%;border:1px solid var(--line);background:var(--white)}
.icon-ring svg{position:absolute;left:8px;top:8px;width:16px;height:16px}
.bubble{position:absolute;width:70px;height:53px;border-radius:7px;color:var(--white);font-size:4.6px;font-weight:700;line-height:1.3;padding:9px 9px}
.bubble::before{content:"";position:absolute;left:-5px;top:22px;border-style:solid;border-width:4px 5px 4px 0;border-color:transparent}
.bubble.blue{background:var(--mid)}
.bubble.blue::before{border-right-color:var(--mid)}
.bubble.cyan{background:var(--cyan)}
.bubble.cyan::before{border-right-color:var(--cyan)}
.footer-line{position:absolute;left:0;right:0;top:201px;text-align:center;font-size:6.5px;line-height:1.3;color:#333}

/* circle diagram */
.big-ring{position:absolute;width:72px;height:72px;border-radius:50%;border:1px solid var(--line);background:var(--white)}
.big-ring svg{position:absolute;left:18px;top:18px;width:36px;height:36px}
.note{position:absolute;width:60px;font-size:4.8px;line-height:1.3;color:var(--line)}
.note.right-aligned{text-align:right}

/* services 2 */
.label{position:absolute;top:140px;width:62px;height:16px;color:var(--white);font-size:7.5px;font-weight:700;text-align:center;line-height:16px}
.label.blue{background:var(--mid)}
.label.cyan{background:var(--cyan)}
.col-text{position:absolute;top:169px;width:62px;font-size:4.8px;line-height:1.3;text-align:center;color:#5a4a4a}

/* contact */
.contact-photo{inset:0;background:linear-gradient(100deg,#dcd7d2 0%,#eeeeee 40%,#c9c3bd 100%)}
.contact-panel{position:absolute;left:167px;top:0;width:140px;height:230px;background:rgba(59,104,166,.82)}
.contact-head{position:absolute;left:167px;top:104px;width:123px;height:22px;background:var(--navy);color:var(--white);font-size:10px;padding-left:23px;line-height:22px}
.contact-card{position:absolute;left:167px;top:126px;width:123px;height:44px;background:rgba(31,59,99,.75);color:var(--white);padding:11px 0 0 22px}
.contact-card strong{display:block;font-size:7px;line-height:9px;font-weight:700;margin-bottom:3px}
.contact-card span{display:block;font-size:5.5px;line-height:7px}
</style>
</head>
<body>

<!-- Cover -->
<section class="slide" style="left:126px;top:115px">
  <div class="photo cover-photo" role="img" aria-label="Photo of a smiling businessman in a checked shirt holding a phone, standing in a bright office"></div>
  <div class="stripe" style="left:72px;width:10px"></div>
  <div class="stripe" style="left:91px;width:4px"></div>
  <div class="stripe" style="left:285px;width:8px"></div>
  <div class="brand-name">KESTRELON</div>
</section>

<!-- Introduction -->
<section class="slide" style="left:468px;top:116px">
  <div class="intro-band"><h2>INTRODUCTION</h2></div>
  <div class="avatar" role="img" aria-label="Portrait photo of the company president"></div>
  <div class="author-name">DANIEL MOREAU</div>
  <div class="author-role">President and Co-Founder</div>
  <div class="intro-text body-text">
    <p>Lorem ipsum dolor sit amet, consectetur adipiscing elit. Nunc dignissim ultricies nisl a semper. Fusce vel ornare ipsum. Sed elit tortor, iaculis eu metus et, rutrum euismod quam. Curabitur neque nisi, hendrerit non felis vel, dapibus lobortis felis. Nulla eu dui sem. Integer eu risus in sem elementum aliquet sed ac libero. Quisque eget feugiat leo.</p>
    <p>Etiam finibus velit eget magna tristique pulvinar. Fusce leo orci, egestas at interdum vel, vulputate eu turpis. Praesent viverra sit amet dui vitae interdum. Suspendisse porttitor venenatis pulvinar. Vivamus rutrum aliquam enim, vitae viverra augue semper a. Nam a velit sed justo consequat pretium non vitae risus. Duis eget turpis vitae felis eleifend sagittis. Lorem ipsum dolor sit amet, consectetur adipiscing</p>
  </div>
</section>

<!-- Grid slide -->
<section class="slide" style="left:126px;top:372px">
  <h2 class="slide-title" style="top:16px">LOREM IPSUM DOLOR SIT AMET</h2>
  <div class="photo" style="left:0;top:41px;width:103px;height:85px;background:linear-gradient(120deg,#c9ced4,#8e949c)" role="img" aria-label="Photo of two business people shaking hands"></div>
  <div class="tile cyan" style="left:102px;top:41px">Nunc consequat, massa vitae dignissim elementum, nisi magna tempor sapien, efficitur luctus metus dolor in enim. Ut placerat et purus eu porttitor. Maecenas quis velit enim.</div>
  <div class="photo" style="left:204px;top:41px;width:103px;height:85px;background:linear-gradient(120deg,#b9aa98,#6f6558)" role="img" aria-label="Photo of a hand holding a smartphone"></div>
  <div class="tile blue" style="left:0;top:126px">Nunc consequat, massa vitae dignissim elementum, nisi magna tempor sapien, efficitur luctus metus dolor in enim. Ut placerat et purus eu porttitor. Maecenas quis velit enim.</div>
  <div class="photo" style="left:102px;top:126px;width:103px;height:85px;background:linear-gradient(120deg,#e8ecef,#8fb6c9)" role="img" aria-label="Photo of a team of medical staff in scrubs"></div>
  <div class="tile blue" style="left:204px;top:126px">Nunc consequat, massa vitae dignissim elementum, nisi magna tempor sapien, efficitur luctus metus dolor in enim. Ut placerat et purus eu porttitor. Maecenas quis velit enim.</div>
</section>

<!-- Our services -->
<section class="slide" style="left:468px;top:369px">
  <h2 class="slide-title" style="top:15px">OUR SERVICES</h2>
  <p class="subtitle" style="top:36px">Lorem ipsum dolor sit amet, consectetur adipiscing elit. Aenean sed tempor lorem. Suspendisse</p>
  <div class="photo" style="left:22px;top:54px;width:153px;height:90px;background:linear-gradient(90deg,#d8d8d8,#a6a3a0)" role="img" aria-label="Photo of a team joining hands in the middle"></div>
  <div class="feature-box">
    <h3>LOREM IPSUM</h3>
    <p>Lorem ipsum dolor sit amet, consectetur adipiscing elit. Aenean sed tempor lorem. Suspendisse varius enim id dolor euismod, quis condimentum risus blandit. Sed imperdiet dolor orci, at pulvinar nisl pharetra et.</p>
  </div>
  <div class="services-text body-text">
    <p>Nunc consequat, massa vitae dignissim elementum, nisi magna tempor sapien, efficitur luctus metus dolor in enim. Ut placerat et purus eu porttitor. Maecenas quis velit enim. Suspendisse mollis diam et ligula laoreet, et commodo eros venenatis. Etiam elementum sollicitudin iaculis. Proin et congue sem, vitae ullamcorper risus. Sed in pretium erat, a finibus urna. Pellentesque habitant morbi tristique senectus et netus et malesuada fames ac turpis egestas.</p>
    <p>Donec interdum nunc eu lacinia viverra. Praesent dapibus erat at elit eleifend consequat. Ut facilisis sem felis, vel tincidunt arcu cursus eu. Vestibulum sed blandit lorem. In pretium diam euismod ipsum fermentum, ultrices semper tortor rhoncus. Sed non lorem enim. Quisque tincidunt nisl at euismod rutrum. Integer ut nibh magna.</p>
  </div>
</section>

<!-- Icon bubbles -->
<section class="slide" style="left:126px;top:625px">
  <h2 class="slide-title" style="top:14px">LOREM IPSUM DOLOR SIT AMET</h2>

  <div class="icon-ring" style="left:25px;top:61px">
    <svg viewBox="0 0 16 16"><path fill="#4f82c8" d="M2 6h3a2 2 0 1 1 4 0h3v3a2 2 0 1 1 0 4v1H2v-3a2 2 0 1 0 0-4z"/></svg>
  </div>
  <div class="bubble blue" style="left:68px;top:51px">Lorem ipsum dolor sit amet consectetur adipiscing elit. Cras bibendum mattis leo, ac efficitur ipsum lobortis non.</div>

  <div class="icon-ring" style="left:159px;top:61px">
    <svg viewBox="0 0 16 16"><path fill="#4f82c8" d="M2 14V8l3-2v2l3-2v2l3-2V3h2v11z"/><rect x="4" y="10" width="2" height="2" fill="#fff"/><rect x="7" y="10" width="2" height="2" fill="#fff"/><rect x="10" y="10" width="2" height="2" fill="#fff"/></svg>
  </div>
  <div class="bubble cyan" style="left:202px;top:51px">Lorem ipsum dolor sit amet consectetur adipiscing elit. Cras bibendum mattis leo, ac efficitur ipsum lobortis non.</div>

  <div class="icon-ring" style="left:25px;top:137px">
    <svg viewBox="0 0 16 16"><circle cx="8" cy="7" r="4" fill="#4f82c8"/><path d="M3 8V6a5 5 0 0 1 10 0v2" fill="none" stroke="#4f82c8" stroke-width="1.4"/><path d="M12 9c0 3-2 4-4 4" fill="none" stroke="#4f82c8" stroke-width="1"/><circle cx="8" cy="13" r="1" fill="#4f82c8"/></svg>
  </div>
  <div class="bubble blue" style="left:68px;top:128px">Lorem ipsum dolor sit amet consectetur adipiscing elit. Cras bibendum mattis leo, ac efficitur ipsum lobortis non.</div>

  <div class="icon-ring" style="left:159px;top:137px">
    <svg viewBox="0 0 16 16"><circle cx="5.5" cy="5" r="2.2" fill="#4f82c8"/><circle cx="10.5" cy="5" r="2.2" fill="#4f82c8"/><path d="M1 14v-3a3 3 0 0 1 3-3h3a3 3 0 0 1 3 3v3z" fill="#4f82c8"/><path d="M9 8h3a3 3 0 0 1 3 3v3H11" fill="#4f82c8"/></svg>
  </div>
  <div class="bubble cyan" style="left:202px;top:128px">Lorem ipsum dolor sit amet consectetur adipiscing elit. Cras bibendum mattis leo, ac efficitur ipsum lobortis non.</div>

  <p class="footer-line">Quarvenne Offers a focused mix of IT, BPM and Professional<br>Services tailored to specific sectors</p>
</section>

<!-- Circle diagram -->
<section class="slide" style="left:468px;top:625px">
  <h2 class="slide-title" style="top:15px">LOREM IPSUM DOLOR SIT AMET</h2>
  <div class="big-ring" style="left:77px;top:62px">
    <svg viewBox="0 0 16 16"><path fill="#6f93c6" d="M2 6h3a2 2 0 1 1 4 0h3v3a2 2 0 1 1 0 4v1H2v-3a2 2 0 1 0 0-4z"/></svg>
  </div>
  <div class="big-ring" style="left:143px;top:62px">
    <svg viewBox="0 0 16 16"><path fill="#3b68a6" d="M2 14V8l3-2v2l3-2v2l3-2V3h2v11z"/><rect x="4" y="10" width="2" height="2" fill="#fff"/><rect x="7" y="10" width="2" height="2" fill="#fff"/><rect x="10" y="10" width="2" height="2" fill="#fff"/></svg>
  </div>
  <div class="big-ring" style="left:113px;top:112px">
    <svg viewBox="0 0 16 16"><circle cx="8" cy="7" r="4" fill="#3b68a6"/><path d="M3 8V6a5 5 0 0 1 10 0v2" fill="none" stroke="#3b68a6" stroke-width="1.4"/><path d="M12 9c0 3-2 4-4 4" fill="none" stroke="#3b68a6" stroke-width="1"/><circle cx="8" cy="13" r="1" fill="#3b68a6"/></svg>
  </div>
  <p class="note right-aligned" style="left:11px;top:82px">Lorem ipsum dolor sit amet consectetur adipiscing elit. Cras bibendum mattis leo, ac efficitur ipsum lobortis non.</p>
  <p class="note" style="left:221px;top:76px">Lorem ipsum dolor sit amet consectetur adipiscing elit. Cras bibendum mattis leo, ac efficitur ipsum lobortis non.</p>
  <p class="note" style="left:193px;top:146px">Lorem ipsum dolor sit amet consectetur adipiscing elit. Cras bibendum mattis leo, ac efficitur ipsum lobortis non.</p>
</section>

<!-- Our services, columns -->
<section class="slide" style="left:126px;top:878px">
  <h2 class="slide-title" style="top:14px">OUR SERVICES</h2>
  <p class="subtitle" style="top:36px">Lorem ipsum dolor sit amet, consectetur adipiscing elit. Aenean sed tempor lorem. Suspendisse</p>
  <div class="photo" style="left:18px;top:49px;width:272px;height:85px;background:linear-gradient(90deg,#6c7a52,#8f6a55 55%,#9a5a48)" role="img" aria-label="Photo of three smiling colleagues in front of a brick wall"></div>
  <div class="label blue" style="left:18px">A</div>
  <div class="label blue" style="left:88px">B</div>
  <div class="label blue" style="left:158px">C</div>
  <div class="label cyan" style="left:228px">D</div>
  <p class="col-text" style="left:18px">Lorem ipsum dolor sit amet, consectetur adipiscing elit. Aenean sed tempor lorem. Suspendisse varius enim id euismod, quis condimentum risus</p>
  <p class="col-text" style="left:88px">Lorem ipsum dolor sit amet, consectetur adipiscing elit. Aenean sed tempor lorem. Suspendisse varius enim id euismod, quis condimentum risus</p>
  <p class="col-text" style="left:158px">Lorem ipsum dolor sit amet, consectetur adipiscing elit. Aenean sed tempor lorem. Suspendisse varius enim id euismod, quis condimentum risus</p>
  <p class="col-text" style="left:228px">Lorem ipsum dolor sit amet, consectetur adipiscing elit. Aenean sed tempor lorem. Suspendisse varius enim id euismod, quis condimentum risus</p>
</section>

<!-- Contact -->
<section class="slide" style="left:468px;top:878px">
  <div class="photo contact-photo" role="img" aria-label="Photo of business colleagues talking at a meeting table"></div>
  <div class="contact-panel"></div>
  <div class="contact-head">CONTACT US</div>
  <div class="contact-card">
    <strong>EMPLOYEE NAME</strong>
    <span>email@quarvennecorp.com</span>
  </div>
</section>

</body>
</html>
```